Business Cards for GPS Technology Business - Logo Supplied

Brelka Technologies Ltd. requires a business card design. Brelka is a startup GPS vehicle fleet tracking vendor. Our hardware/software helps business fleets be more productive and reduce operating costs. Our systems utilize a mix of GPS satellite, cell network and web technologies.
We would like to see a double sided original design utilizing our existing logo. Please use whatever colors will work with the blue logo.
As a business, we want to project the image of friendly and approachable lifetime business partners and advisors to our customers - “someone you can trust”. Words customers will use to describe us will include: knowledgeable, supportive, trustworthy and honest.
We will also require Viewtube, Chirpnet, Pagebook and Lookup+ backgrounds. Winner will be first in line to quote for this work (separate project).
Updates
Hello designers!
Target Market(s)
Target audience are working owners and managers of vehicle fleets. Usually male, age 30 to 60. Often have a trades background.
Industry/Entity Type
Business
Font styles to use
Requirements
Must have
- Please use the following dummy data for the design:
name: Ned Brelka
title: Director
address: 2389 Marlow Drive
city: Kelvaton, BC
postal code: K7P 2T4
cell phone number: 555-214-7730
business number: 555-309-4412
toll free number: 1-800-555-0199
web site address: www.brelka-example.com
tagline: GPS Fleet Tracking Specialists
Nice to have
- Abstract imagery relating to GPS tracking / fleet vehicles / technology
Should not have
- Do not use serif fonts.

```html
<!DOCTYPE html>
<html lang="en">
<head>
<meta charset="utf-8">
<title>Brelka Technologies – Business Card</title>
<link rel="stylesheet" href="https://fonts.googleapis.com/css2?family=Roboto:wght@400;700;900&family=Roboto+Condensed:wght@400;700&display=swap">
<style>
  :root {
    --brand-blue: #1b6ab9;
    --paper: #ffffff;
    --paper-shade: #e4e6e9;
    --ink-grey: #555a60;
    --backdrop: #ecebe8;
  }
  * { box-sizing: border-box; margin: 0; padding: 0; }
  html, body { width: 1200px; height: 939px; overflow: hidden; }
  body {
    background: var(--backdrop);
    font-family: "Roboto", Arial, sans-serif;
    position: relative;
  }
  .card {
    position: absolute;
    width: 460px;
    height: 263px;
    overflow: hidden;
    background: linear-gradient(135deg, var(--paper) 40%, var(--paper-shade));
    box-shadow: 0 6px 18px rgba(0,0,0,.18);
  }
  .card-front { left: 573px; top: 193px; }
  .card-back  { left: 287px; top: 600px; }
  .card-shapes { position: absolute; inset: 0; }

  .holder {
    position: absolute; right: 28px; top: 22px;
    font-size: 15px; color: var(--ink-grey);
  }
  .holder-name { font-weight: 700; }
  .holder-sep { color: var(--brand-blue); margin: 0 5px; }
  .wordmark {
    position: absolute;
    font-family: "Roboto", Arial, sans-serif;
    font-weight: 900;
    letter-spacing: 1px;
    line-height: 1;
  }
  .card-front .wordmark { right: 26px; top: 52px; font-size: 46px; color: var(--brand-blue); }
  .card-back .wordmark { left: 40px; top: 148px; font-size: 54px; color: var(--paper); }

  .contact {
    position: absolute; right: 26px; top: 136px;
    font-family: "Roboto Condensed", Arial, sans-serif;
    font-size: 10.5px; color: var(--ink-grey);
    text-align: right; line-height: 17px;
  }
  .contact-item { margin-left: 10px; white-space: nowrap; }
  .contact-icon {
    display: inline-block; width: 9px; height: 9px; border-radius: 50%;
    background: var(--brand-blue); margin-right: 3px; vertical-align: -1px;
  }
  .tagline {
    position: absolute;
    font-family: "Roboto Condensed", Arial, sans-serif;
    text-transform: uppercase; color: var(--paper);
    letter-spacing: .5px;
  }
  .card-front .tagline { right: 26px; top: 229px; font-size: 12.5px; }
  .card-back .tagline { left: 42px; top: 206px; font-size: 13px; letter-spacing: 1px; }
</style>
</head>
<body>

<section class="card card-front" aria-label="Business card front">
  <svg class="card-shapes" viewBox="0 0 460 263" width="460" height="263" aria-hidden="true">
    <path d="M0 0 H178 C90 40 20 130 6 263 H0 Z" fill="var(--brand-blue)"/>
    <path d="M160 263 C175 230 190 215 235 212 H460 V263 Z" fill="var(--brand-blue)"/>
  </svg>
  <p class="holder"><span class="holder-name">Ned Brelka</span><span class="holder-sep">|</span>Director</p>
  <p class="wordmark">BRELKA</p>
  <div class="contact">
    <p>
      <span class="contact-item"><span class="contact-icon"></span>555-309-4412</span>
      <span class="contact-item"><span class="contact-icon"></span>555-214-7730</span>
      <span class="contact-item"><span class="contact-icon"></span>1-800-555-0199</span>
    </p>
    <p>
      <span class="contact-item"><span class="contact-icon"></span>2389 Marlow Drive, Kelvaton, BC, K7P 2T4</span>
      <span class="contact-item"><span class="contact-icon"></span>www.brelka-example.com</span>
    </p>
  </div>
  <p class="tagline">GPS Fleet Tracking Specialists</p>
</section>

<section class="card card-back" aria-label="Business card back">
  <svg class="card-shapes" viewBox="0 0 460 263" width="460" height="263" aria-hidden="true">
    <rect width="460" height="263" fill="var(--brand-blue)"/>
    <path d="M0 0 H290 C262 4 262 87 210 87 H0 Z" fill="var(--paper-shade)"/>
    <path d="M460 60 C440 150 400 225 345 263 H460 Z" fill="var(--paper)"/>
  </svg>
  <p class="wordmark">BRELKA</p>
  <p class="tagline">GPS Fleet Tracking Specialists</p>
</section>

</body>
</html>
```